Harvest Quorum Lumera LLC

I am starting/launching my IT Consulting company in the Washington DC area. I just finished the logo design with ArtHive with the color palette in the attach. The mission and vision of the company is to help clients (mainly Federal Govt) "lumera" their business digital and business transformation journey . The name is intentional to incorporate my HQ initials. I would like to have a PPT template for the company with a few different pages so it covers a text, table grids. I found a Velotrix PPT Sales Pitch template with new/modern design that Im attaching here as an example. I would like the pages content to model after this one, but the design can be what you come up with. I don't necessarily have to have a color accent line at top of the slide (it seems interfere with page real estate). The pictures will need to be more relevant to IT modernization, transformation, data/AI, digital workforce, consulting. The color team can be white background with light/darker gray, black, ivory and the 2 tones of teals in the logos be the accent. I would use the more muted teal more and the brighter teal to be stronger accent as needed. I found this website template color theme and look and feel to be quite fitting to what I envision
https://www.plumnestsites.com/website-templates/professional-services
Thank you

```html
<!DOCTYPE html>
<html lang="en">
<head>
<meta charset="utf-8">
<title>HQ Lumera – Company Presentation Template</title>
<link href="https://fonts.googleapis.com/css2?family=Poppins:ital,wght@0,400;0,500;0,600;0,700;0,800;1,400&family=Oswald:wght@600;700&display=swap" rel="stylesheet">
<style>
:root{
  --teal:#2a7f7a;
  --teal-light:#86b7b5;
  --teal-deep:#1f5f5c;
  --ink:#111111;
  --grey:#6b6b6b;
  --board:#dadada;
  --white:#ffffff;
}
*{margin:0;padding:0;box-sizing:border-box}
html,body{width:1043px;height:1200px;overflow:hidden;background:var(--board)}
body{font-family:'Poppins',sans-serif;color:var(--ink)}
.board{position:absolute;left:0;top:0;width:1792px;height:2061px;transform:scale(0.582);transform-origin:0 0;background:var(--board)}
.slide{position:absolute;width:534px;height:300px;background:var(--white);overflow:hidden;box-shadow:0 3px 8px rgba(0,0,0,.28)}
.slide > *{position:absolute}
.page-no{right:16px;bottom:10px;font-size:7px;color:#333}
.photo{background:linear-gradient(135deg,#0f2a33,#1f5f5c 55%,#2b3e4a)}
.photo.light{background:linear-gradient(135deg,#e7ecef,#b9c6cc 60%,#7c8d95)}
.fine{font-size:6.5px;line-height:1.35;color:var(--grey)}
.fine.white{color:#e6f1f0}
.h-bold{font-weight:700;line-height:1.1}
.teal{color:var(--teal)}
.bar-teal{background:var(--teal)}
.bar-ink{background:var(--ink)}
.dash{width:26px;height:2px;background:var(--ink)}
.dash::after{content:"";position:absolute;left:30px;top:0;width:6px;height:2px;background:var(--teal)}
.num-item{display:flex;gap:7px;color:#fff}
.num-item b.n{display:inline-block;min-width:18px;height:18px;background:var(--white);color:var(--ink);font-size:11px;text-align:center;line-height:18px}
.num-item .t{font-size:10px;font-weight:600;line-height:1.1}
.icon-dot{border-radius:50%;background:var(--teal)}
.proj .t{font-size:11px;font-weight:600}
</style>
</head>
<body>
<div class="board">

<!-- 1 Cover -->
<section class="slide" style="left:67px;top:75px">
  <div class="bar-teal" style="left:12px;top:12px;width:13px;height:13px"></div>
  <div class="h-bold" style="left:33px;top:48px;font-size:21px;font-weight:600;letter-spacing:.5px">HQ LUMERA</div>
  <div class="teal" style="left:31px;top:106px;font-size:13px;font-weight:500">COMPANY</div>
  <div style="left:30px;top:118px;font-family:'Oswald',sans-serif;font-weight:700;font-size:44px;line-height:1.1">BUSINESS</div>
  <div class="teal" style="left:31px;top:170px;font-size:19px;font-weight:600">MARKETING</div>
  <div class="dash" style="left:33px;top:207px"></div>
  <div style="left:31px;top:219px;font-size:12px;font-style:italic">Presentation</div>
  <div class="fine" style="left:31px;top:236px;width:140px;font-style:italic">Lorem ipsum dolor sit amet, consectetuer adipiscing elit, sed diam nonum</div>
  <svg style="left:32px;top:268px" width="34" height="8"><circle cx="3" cy="4" r="3"/><circle cx="14" cy="4" r="3" fill="#2a7f7a"/><circle cx="25" cy="4" r="3"/></svg>
  <div class="photo" role="img" aria-label="Photo of a consultant working on a laptop with digital network overlay" style="left:224px;top:0;width:310px;height:245px"></div>
  <div class="bar-teal" style="left:224px;top:245px;width:310px;height:55px"></div>
  <div style="left:224px;top:265px;width:310px;text-align:center;color:#fff;font-size:10px;letter-spacing:4px">WWW.WEBSITE.COM</div>
</section>

<!-- 2 Agenda -->
<section class="slide" style="left:630px;top:75px">
  <div class="photo" role="img" aria-label="Photo of hands holding a glowing digital globe" style="left:72px;top:0;width:188px;height:300px"></div>
  <div class="bar-teal" style="left:46px;top:43px;width:54px;height:213px"></div>
  <div style="left:46px;top:43px;width:54px;height:213px;display:flex;align-items:center;justify-content:center"><span style="transform:rotate(90deg);color:#fff;font-weight:700;font-size:27px;white-space:nowrap">Agenda</span></div>
  <div style="left:285px;top:62px;width:220px">
    <div style="font-size:10.5px;font-weight:500">1. Lorem ipsum</div><div class="fine" style="margin:2px 0 0 8px">Lorem ipsum dolor sit amet, consectetuer adipiscing elit, sed diam nonummy nibh euismod tincid</div>
    <div style="font-size:10.5px;font-weight:500;margin-top:16px">2. Lorem ipsum</div><div class="fine" style="margin:2px 0 0 8px">Lorem ipsum dolor sit amet, consectetuer adipiscing elit, sed diam nonummy nibh euismod tincid</div>
    <div style="font-size:10.5px;font-weight:500;margin-top:16px">3. Lorem ipsum</div><div class="fine" style="margin:2px 0 0 8px">Lorem ipsum dolor sit amet, consectetuer adipiscing elit, sed diam nonummy nibh euismod tincid</div>
    <div style="font-size:10.5px;font-weight:500;margin-top:14px">4. Lorem ipsum</div><div class="fine" style="margin:2px 0 0 8px">Lorem ipsum dolor sit amet, consectetuer adipiscing elit, sed diam nonummy nibh euismod tincid</div>
  </div>
  <div class="bar-teal" style="left:526px;top:50px;width:8px;height:200px"></div>
  <div class="page-no">2</div>
</section>

<!-- 3 -->
<section class="slide" style="left:1192px;top:75px">
  <div class="bar-teal" style="left:0;top:82px;width:16px;height:148px"></div>
  <div class="h-bold" style="left:29px;top:92px;font-size:31px;font-weight:800;line-height:1.25">Text<br><span class="teal">Added</span><br>Here</div>
  <div class="photo" role="img" aria-label="Photo of a human hand shaking a digital hand" style="left:170px;top:48px;width:364px;height:145px"></div>
  <div class="bar-teal" style="left:236px;top:143px;width:106px;height:32px;color:#fff;font-size:16px;font-weight:600;text-align:center;line-height:32px">Text Here</div>
  <div style="left:236px;top:175px;width:106px;height:97px;background:#fff;box-shadow:0 1px 4px rgba(0,0,0,.2);padding:5px 8px" class="fine">Lorem ipsum dolor sit amet, consectetuer adipiscing elit, sed diam nonummy nibh euismod tincidunt ut laoreet dolore magna aliquam erat volutpat.<br><br>Ut wisi enim ad minim veniam, quis nostrud exerci tation ullamcorper suscipit commodo conse</div>
  <div class="bar-teal" style="left:370px;top:143px;width:106px;height:32px;color:#fff;font-size:16px;font-weight:600;text-align:center;line-height:32px">Text Here</div>
  <div style="left:370px;top:175px;width:106px;height:97px;background:#fff;box-shadow:0 1px 4px rgba(0,0,0,.2);padding:5px 8px" class="fine">Lorem ipsum dolor sit amet, consectetuer adipiscing elit, sed diam nonummy nibh euismod tincidunt ut laoreet dolore magna aliquam erat volutpat.<br><br>Ut wisi enim ad minim veniam, quis nostrud exerci tation ullamcorper suscipit commodo conse</div>
  <div class="page-no">3</div>
</section>

<!-- 4 -->
<section class="slide" style="left:67px;top:398px">
  <div class="bar-teal" style="left:0;top:0;width:14px;height:300px"></div>
  <div class="bar-ink" style="left:420px;top:0;width:114px;height:95px"></div>
  <div class="bar-teal" style="left:236px;top:178px;width:136px;height:122px"></div>
  <div class="photo light" role="img" aria-label="Photo of a smiling support agent with headset at a computer" style="left:259px;top:55px;width:239px;height:190px"></div>
  <div class="h-bold" style="left:50px;top:60px;font-size:17px;font-weight:700;line-height:1.2">Lorem Ipsum<br>Dolor Sit<br>Ametkeeper.</div>
  <div class="dash" style="left:50px;top:133px"></div>
  <div class="fine" style="left:50px;top:143px;width:170px">Lorem ipsum dolor sit amet, consectetuer adipiscing elit, sed diam nonummy nibh euismod tincidunt ut laoreet dolore magna aliquam erat volutpat. Ut wisi it lob edo consequat. Duis autem lore te feugait nulla facilisi.<br><br>Lorem ipsum dolor sit amet, cons ectetuer adipiscing elit, sed diam nonim ad minim veniam, quis nostrud exerci tation ullamcorper</div>
  <div class="page-no">4</div>
</section>

<!-- 5 -->
<section class="slide" style="left:630px;top:398px">
  <div class="bar-ink" style="left:0;top:0;width:14px;height:300px"></div>
  <div class="photo" role="img" aria-label="Photo of hands typing with AI interface graphics" style="left:290px;top:25px;width:208px;height:248px"></div>
  <div class="bar-teal" style="left:236px;top:90px;width:119px;height:118px;color:#fff;font-family:'Oswald',sans-serif;font-size:74px;font-weight:600;text-align:center;line-height:116px">01</div>
  <div style="left:48px;top:102px;font-size:23px;font-weight:700">Part <span class="teal">One</span></div>
  <div class="fine" style="left:48px;top:138px;width:165px">Lorem ipsum dolor sit amet, laoreet dolore magna aliquam erat volutpat. Ut wisi it lob edo consequat. Duis autem lore te feugait nulla facilisi.<br><br>Lorem ipsum dolor sit amet, cons ectetuer adipiscing elit, sed diam nonim ad minim veniam, quis nostrud exerci tation ullamcorper</div>
  <div class="page-no">5</div>
</section>

<!-- 6 -->
<section class="slide" style="left:1192px;top:398px">
  <div class="bar-teal" style="left:0;top:20px;width:10px;height:87px"></div>
  <div class="h-bold" style="left:27px;top:20px;font-size:22px;font-weight:700;line-height:1.2">Lorem<br>Dolor Sit<br>Consectetuer</div>
  <div class="fine" style="left:29px;top:122px;width:210px">Lorem ipsum dolor sit amet, consectetuer adipiscing elit, sed diam nonummy nibh euismod tincidunt ut laoreet dolore magna aliquam erat volutpat.Ut wisi enim ad minim veniam, quis nostrud exerci tation ullamcorper suscipit</div>
  <div class="teal" style="left:320px;top:58px;font-size:17px;font-weight:700">768K</div>
  <div style="left:309px;top:81px;font-size:10px;font-weight:600">Lorem Ipsum</div>
  <div class="fine" style="left:309px;top:95px;width:95px">Lorem ipsum dolor sit amet, consectetuer elit.</div>
  <div class="teal" style="left:437px;top:58px;font-size:17px;font-weight:700">423K</div>
  <div style="left:426px;top:81px;font-size:10px;font-weight:600">Lorem Ipsum</div>
  <div class="fine" style="left:426px;top:95px;width:95px">Lorem ipsum dolor sit amet, consectetuer elit.</div>
  <div class="bar-teal" style="left:112px;top:197px;width:422px;height:103px"></div>
  <div class="bar-teal" style="left:304px;top:160px;width:230px;height:37px;color:#fff;font-size:15px;font-weight:600;padding-left:15px;line-height:37px">Text Added Here</div>
  <div class="photo" role="img" aria-label="Photo of hands on a laptop with glowing data interface" style="left:124px;top:197px;width:376px;height:103px"></div>
  <div class="page-no" style="color:#fff">6</div>
</section>

<!-- 7 Bar chart -->
<section class="slide" style="left:67px;top:724px">
  <div class="h-bold" style="left:28px;top:20px;font-size:17px;line-height:1.25">Text<br>Added Hare</div>
  <div class="dash" style="left:28px;top:71px"></div>
  <div class="bar-ink" style="left:0;top:90px;width:172px;height:178px"></div>
  <div style="left:30px;top:105px;width:130px;display:flex;flex-direction:column;gap:12px">
    <div class="num-item"><b class="n">1.</b><div><div class="t">Lorem Ipsum</div><div class="fine white" style="font-size:5.8px">Lorem ipsum dolor sit amet, consectetuer adipiscing elit, sed diam nonummy nibh euismod tincid</div></div></div>
    <div class="num-item"><b class="n">2.</b><div><div class="t">Lorem Ipsum</div><div class="fine white" style="font-size:5.8px">Lorem ipsum dolor sit amet, consectetuer adipiscing elit, sed diam nonummy nibh euismod tincid</div></div></div>
    <div class="num-item"><b class="n">3.</b><div><div class="t">Lorem Ipsum</div><div class="fine white" style="font-size:5.8px">Lorem ipsum dolor sit amet, consectetuer adipiscing elit, sed diam nonummy nibh euismod tincid</div></div></div>
  </div>
  <svg style="left:190px;top:60px" width="330" height="200" font-family="Poppins, sans-serif" font-size="7" fill="#333">
    <line x1="10" y1="165" x2="320" y2="165" stroke="#ccc"/>
    <g>
      <rect x="17" y="40.3" width="8" height="124.7" fill="#2a7f7a"/><text x="13" y="36">43%</text>
      <rect x="29" y="95.4" width="8" height="69.6" fill="#86b7b5"/><text x="27" y="91">24%</text>
      <rect x="41" y="107" width="8" height="58" fill="#111"/><text x="41" y="103">20%</text>
      <text x="33" y="178">1</text>
      <rect x="97" y="92.5" width="8" height="72.5" fill="#2a7f7a"/><text x="92" y="88">25%</text>
      <rect x="109" y="37.4" width="8" height="127.6" fill="#86b7b5"/><text x="108" y="33">44%</text>
      <rect x="121" y="107" width="8" height="58" fill="#111"/><text x="122" y="103">20%</text>
      <text x="113" y="178">2</text>
      <rect x="177" y="63.5" width="8" height="101.5" fill="#2a7f7a"/><text x="172" y="59">35%</text>
      <rect x="189" y="112.8" width="8" height="52.2" fill="#86b7b5"/><text x="188" y="108">18%</text>
      <rect x="201" y="78" width="8" height="87" fill="#111"/><text x="201" y="74">30%</text>
      <text x="193" y="178">3</text>
      <rect x="254" y="34.5" width="8" height="130.5" fill="#2a7f7a"/><text x="250" y="30">45%</text>
      <rect x="266" y="83.8" width="8" height="81.2" fill="#86b7b5"/><text x="266" y="79">28%</text>
      <rect x="278" y="20" width="8" height="145" fill="#111"/><text x="278" y="16">50%</text>
      <text x="270" y="178">4</text>
    </g>
    <g font-size="6"><rect x="105" y="189" width="4" height="4" fill="#2a7f7a"/><text x="111" y="193">Series1</text><rect x="140" y="189" width="4" height="4" fill="#86b7b5"/><text x="146" y="193">Series2</text><rect x="175" y="189" width="4" height="4" fill="#111"/><text x="181" y="193">Series3</text></g>
  </svg>
  <div class="bar-teal" style="left:525px;top:35px;width:9px;height:235px"></div>
  <div class="page-no">7</div>
</section>

<!-- 8 Donuts -->
<section class="slide" style="left:630px;top:724px">
  <div class="bar-teal" style="left:0;top:35px;width:8px;height:235px"></div>
  <div class="h-bold" style="left:0;top:20px;width:534px;text-align:center;font-size:16px">Text Added Hare</div>
  <div class="dash" style="left:245px;top:48px"></div>
  <div class="fine" style="left:95px;top:62px;width:344px;text-align:center">Lorem ipsum dolor sit amet, consectetuer adipiscing elit, sed diam nonummy nibh euismod tincidunt ut laoreet dolore magna aliquam erat volutpat. Ut wisi enim ad minim veniam, quis nostrud exerci tation ullamcorper suscipit lobortis nisl ut aliquip ex ea commodo consequat. Duis autem vel eum iriure</div>
  <svg style="left:70px;top:115px" width="400" height="130" font-family="Poppins, sans-serif">
    <g transform="translate(60,55)"><circle r="43" fill="none" stroke="#eee" stroke-width="5"/><circle r="43" fill="none" stroke="#2a7f7a" stroke-width="7" stroke-dasharray="135 270" transform="rotate(-90)"/><text text-anchor="middle" y="8" font-size="22" font-weight="600" fill="#111">50%</text></g>
    <g transform="translate(198,55)"><circle r="43" fill="none" stroke="#eee" stroke-width="5"/><circle r="43" fill="none" stroke="#86b7b5" stroke-width="7" stroke-dasharray="202.6 270" transform="rotate(-90)"/><text text-anchor="middle" y="8" font-size="22" font-weight="600" fill="#111">75%</text></g>
    <g transform="translate(336,55)"><circle r="43" fill="none" stroke="#eee" stroke-width="5"/><circle r="43" fill="none" stroke="#222" stroke-width="7" stroke-dasharray="108 270" transform="rotate(-90)"/><text text-anchor="middle" y="8" font-size="22" font-weight="600" fill="#111">40%</text></g>
  </svg>
  <div class="fine" style="left:75px;top:230px;width:110px;text-align:center">Lorem ipsom dolor amet amet consectetur dolor</div>
  <div class="fine" style="left:213px;top:230px;width:110px;text-align:center">Lorem ipsom dolor amet amet consectetur dolor</div>
  <div class="fine" style="left:351px;top:230px;width:110px;text-align:center">Lorem ipsom dolor amet amet consectetur dolor</div>
  <div class="page-no">8</div>
</section>

<!-- 9 Cycle -->
<section class="slide" style="left:1192px;top:724px">
  <div class="h-bold" style="left:27px;top:20px;font-size:17px;line-height:1.25">Text<br>Added Hare</div>
  <div class="dash" style="left:27px;top:71px"></div>
  <div class="fine" style="left:27px;top:85px;width:160px">Lorem ipsum dolor sit amet, consectetuer adipiscing elit, sed diam nonummy nibh .<br><br>Ut wisi enim ad minim veniam, quis nostrud exerci tation ullamcorper suscipit lobortis. Ut wisi enim ad minim veniam, quis nostrud exerci tation ullamcorper suscipit</div>
  <div class="bar-teal" style="left:0;top:168px;width:172px;height:100px"></div>
  <div style="left:15px;top:178px;width:150px;color:#fff">
    <div style="font-size:9.5px;font-weight:600">● Lorem Ipsum</div><div class="fine white" style="font-size:5.8px;margin-left:10px">Lorem ipsum dolor sit amet, consectetuer adipiscing elit, sed diam nonummy nibh euismod tincidunt ut laoreet</div>
    <div style="font-size:9.5px;font-weight:600;margin-top:8px">● Lorem Ipsum</div><div class="fine white" style="font-size:5.8px;margin-left:10px">Lorem ipsum dolor sit amet, consectetuer adipiscing elit, sed diam nonummy nibh euismod tincidunt ut laoreet</div>
  </div>
  <svg style="left:210px;top:40px" width="320" height="220" font-family="Poppins, sans-serif" fill="#111">
    <path d="M 195 15 A 88 88 0 1 0 110 192" fill="none" stroke="#2a2a2a" stroke-width="6" transform="translate(0,0)"/>
    <path d="M 52 60 L 36 98 L 68 88 Z" fill="#2a2a2a" transform="rotate(15 52 80)"/>
    <path d="M 110 192 Q 160 215 175 178" fill="none" stroke="#2a2a2a" stroke-width="6"/>
    <circle cx="195" cy="52" r="28" fill="#fff" stroke="#2a7f7a" stroke-width="4"/><circle cx="195" cy="52" r="20" fill="#2a7f7a"/><circle cx="193" cy="50" r="5" fill="none" stroke="#fff" stroke-width="2"/><line x1="197" y1="54" x2="202" y2="59" stroke="#fff" stroke-width="2"/>
    <circle cx="212" cy="133" r="24" fill="#fff" stroke="#2a7f7a" stroke-width="4"/><circle cx="212" cy="133" r="16" fill="#2a7f7a"/><circle cx="212" cy="133" r="5" fill="#fff"/>
    <circle cx="168" cy="190" r="17" fill="#fff" stroke="#2a7f7a" stroke-width="3"/><circle cx="168" cy="190" r="11" fill="#2a7f7a"/>
    <circle cx="63" cy="147" r="11" fill="#fff" stroke="#2a7f7a" stroke-width="3"/><circle cx="63" cy="147" r="6" fill="#2a7f7a"/>
    <circle cx="40" cy="128" r="5" fill="#2a2a2a"/>
    <rect x="90" y="70" width="4" height="14"/><rect x="96" y="64" width="4" height="20"/><rect x="102" y="72" width="4" height="12"/>
    <text x="98" y="98" text-anchor="middle" font-size="8" font-weight="600">MAIN TITLE</text>
    <text x="98" y="107" text-anchor="middle" font-size="4.5" fill="#666">Lorem ipsum dolor sit amet,</text>
    <text x="98" y="113" text-anchor="middle" font-size="4.5" fill="#666">sed diam nonummy nibh</text>
    <text x="228" y="28" font-size="6" font-weight="700" font-style="italic">85%</text>
    <text x="247" y="43" font-size="7" font-weight="600">Your Title</text>
    <text x="240" y="52" font-size="4.5" fill="#666">Lorem ipsum dolor sit amet,</text>
    <text x="240" y="58" font-size="4.5" fill="#666">sed diam nonummy nibh</text>
    <text x="159" y="115" font-size="6" font-weight="700" font-style="italic">80%</text>
    <text x="262" y="119" font-size="7" font-weight="600">Your Title</text>
    <text x="248" y="128" font-size="4.5" fill="#666">Lorem ipsum dolor sit amet,</text>
    <text x="248" y="134" font-size="4.5" fill="#666">sed diam nonummy nibh</text>
    <text x="85" y="150" font-size="6" font-weight="700" font-style="italic">50%</text>
    <text x="0" y="168" font-size="7" font-weight="600">Your Title</text>
    <text x="-8" y="177" font-size="4.5" fill="#666">Lorem ipsum dolor sit amet,</text>
    <text x="-8" y="183" font-size="4.5" fill="#666">sed diam nonummy nibh</text>
    <text x="238" y="185" font-size="7" font-weight="600">Your Title</text>
    <text x="225" y="194" font-size="4.5" fill="#666">Lorem ipsum dolor sit amet,</text>
    <text x="225" y="200" font-size="4.5" fill="#666">sed diam nonummy nibh</text>
    <text x="190" y="210" font-size="6" font-weight="700" font-style="italic">75%</text>
  </svg>
  <div class="bar-teal" style="left:525px;top:35px;width:9px;height:235px"></div>
  <div class="page-no">9</div>
</section>

<!-- 10 Service -->
<section class="slide" style="left:67px;top:1051px">
  <div class="bar-teal" style="left:0;top:0;width:95px;height:110px"></div>
  <div class="photo" role="img" aria-label="Photo of hands typing on a laptop with AI icon overlay" style="left:33px;top:32px;width:201px;height:236px"></div>
  <div class="bar-teal" style="left:75px;top:232px;width:118px;height:36px;color:#fff;font-size:16px;font-weight:600;text-align:center;line-height:36px">Service</div>
  <div class="bar-teal" style="left:525px;top:35px;width:9px;height:235px"></div>
  <svg style="left:262px;top:54px" width="44" height="200">
    <g fill="none" stroke="#fff" stroke-width="1.5">
      <circle cx="22" cy="22" r="21" fill="#2a7f7a" stroke="none"/><circle cx="22" cy="22" r="9"/><circle cx="22" cy="22" r="4"/><line x1="22" y1="22" x2="33" y2="11"/>
      <circle cx="22" cy="98" r="21" fill="#2a7f7a" stroke="none"/><circle cx="22" cy="98" r="9"/><circle cx="22" cy="98" r="4"/><line x1="22" y1="98" x2="33" y2="87"/>
      <circle cx="22" cy="176" r="21" fill="#2a7f7a" stroke="none"/><circle cx="22" cy="176" r="9"/><circle cx="22" cy="176" r="4"/><line x1="22" y1="176" x2="33" y2="165"/>
    </g>
  </svg>
  <div class="proj" style="left:317px;top:54px;width:185px"><div class="t">Project name</div><div class="fine">Lorem ipsum dolor sit amet, nec an dictas equidem appellantur, ut has commune accommodare. Mea illum. Iudus solet idpro.</div></div>
  <div class="proj" style="left:317px;top:131px;width:185px"><div class="t">Project name</div><div class="fine">Lorem ipsum dolor sit amet, nec an dictas equidem appellantur, ut has commune accommodare. Mea illum. Iudus solet idpro.</div></div>
  <div class="proj" style="left:317px;top:209px;width:185px"><div class="t">Project name</div><div class="fine">Lorem ipsum dolor sit amet, nec an dictas equidem appellantur, ut has commune accommodare. Mea illum. Iudus solet idpro.</div></div>
  <div class="page-no">10</div>
</section>

<!-- 11 SWOT -->
<section class="slide" style="left:630px;top:1051px">
  <div class="h-bold" style="left:22px;top:17px;font-size:16px">Text Added Hare</div>
  <div class="dash" style="left:22px;top:43px"></div>
  <div class="bar-teal" style="left:526px;top:35px;width:8px;height:235px"></div>
  <svg style="left:120px;top:60px" width="300" height="205" font-family="Poppins, sans-serif">
    <line x1="148" y1="8" x2="148" y2="195" stroke="#888" stroke-dasharray="2 3"/>
    <line x1="50" y1="101" x2="246" y2="101" stroke="#888" stroke-dasharray="2 3"/>
    <circle cx="108" cy="60" r="36" fill="#2a7f7a"/><text x="108" y="72" text-anchor="middle" fill="#fff" font-size="30" font-style="italic" font-weight="500">S</text>
    <circle cx="190" cy="60" r="36" fill="#2a7f7a"/><text x="190" y="72" text-anchor="middle" fill="#fff" font-size="30" font-style="italic" font-weight="500">W</text>
    <circle cx="108" cy="142" r="36" fill="#2a7f7a"/><text x="108" y="154" text-anchor="middle" fill="#fff" font-size="30" font-style="italic" font-weight="500">O</text>
    <circle cx="190" cy="142" r="36" fill="#2a7f7a"/><text x="190" y="154" text-anchor="middle" fill="#fff" font-size="30" font-style="italic" font-weight="500">T</text>
    <circle cx="148" cy="101" r="34" fill="#111" stroke="#fff" stroke-width="2"/><text x="148" y="104" text-anchor="middle" fill="#fff" font-size="7.5" font-style="italic">ANALYSIS</text>
  </svg>
  <div style="left:132px;top:70px;width:80px"><div style="font-size:7px;font-weight:600;font-style:italic">STRENGTHS</div><div class="fine" style="font-size:5.5px">• Good location<br>• Very affordable prices<br>• Variety of activities<br>• Personal trainer</div></div>
  <div style="left:350px;top:68px;width:80px"><div style="font-size:7px;font-weight:600;font-style:italic">WEAKNESSES</div><div class="fine" style="font-size:5.5px">• Not many promotions during the year<br>• Small fitness training rooms<br>• Presence in social networks can be improved</div></div>
  <div style="left:128px;top:182px;width:80px"><div style="font-size:7px;font-weight:600;font-style:italic">OPPORTUNITIES</div><div class="fine" style="font-size:5.5px">• Hiring more graphic designers and marketing members<br>• An app can be practical to track results, find information about nutrition and view workout statistics</div></div>
  <div style="left:356px;top:178px;width:80px"><div style="font-size:7px;font-weight:600;font-style:italic">THREATS</div><div class="fine" style="font-size:5.5px">• Others gyms have more space to workout and running clubs<br>• There are many free fitness app<br>• Principal competitors have nutricionist</div></div>
  <div class="page-no">11</div>
</section>

<!-- 12 Hub -->
<section class="slide" style="left:1192px;top:1051px">
  <div class="bar-teal" style="left:0;top:35px;width:8px;height:235px"></div>
  <svg style="left:40px;top:60px" width="230" height="190">
    <circle cx="77" cy="90" r="68" fill="#fff" stroke="#111" stroke-width="6"/>
    <circle cx="77" cy="90" r="58" fill="#2a7f7a"/>
    <path d="M 150 60 L 178 20 L 220 20 M 150 90 L 220 90 M 150 120 L 178 160 L 220 160" fill="none" stroke="#111" stroke-width="1"/>
  </svg>
  <div style="left:57px;top:115px;width:120px;text-align:center;color:#fff;font-size:17px;font-weight:600;line-height:1.15">Text<br>Added<br>Hare</div>
  <svg style="left:266px;top:56px" width="44" height="200">
    <g fill="none" stroke="#fff" stroke-width="1.5">
      <circle cx="22" cy="22" r="21" fill="#2a7f7a" stroke="none"/><circle cx="22" cy="22" r="9"/><circle cx="22" cy="22" r="4"/><line x1="22" y1="22" x2="33" y2="11"/>
      <circle cx="22" cy="92" r="21" fill="#2a7f7a" stroke="none"/><circle cx="22" cy="92" r="9"/><circle cx="22" cy="92" r="4"/><line x1="22" y1="92" x2="33" y2="81"/>
      <circle cx="22" cy="166" r="21" fill="#2a7f7a" stroke="none"/><circle cx="22" cy="166" r="9"/><circle cx="22" cy="166" r="4"/><line x1="22" y1="166" x2="33" y2="155"/>
    </g>
  </svg>
  <div class="proj" style="left:331px;top:53px;width:185px"><div class="t">Project name</div><div class="fine">Lorem ipsum dolor sit amet, nec an dictas equidem appellantur, ut has commune accommodare. Mea illum. Iudus solet idpro.</div></div>
  <div class="proj" style="left:331px;top:125px;width:185px"><div class="t">Project name</div><div class="fine">Lorem ipsum dolor sit amet, nec an dictas equidem appellantur, ut has commune accommodare. Mea illum. Iudus solet idpro.</div></div>
  <div class="proj" style="left:331px;top:200px;width:185px"><div class="t">Project name</div><div class="fine">Lorem ipsum dolor sit amet, nec an dictas equidem appellantur, ut has commune accommodare. Mea illum. Iudus solet idpro.</div></div>
  <div class="page-no">12</div>
</section>

<!-- 13 Timeline -->
<section class="slide" style="left:67px;top:1375px">
  <div class="bar-ink" style="left:0;top:23px;width:280px;height:30px;color:#fff;font-size:18px;font-weight:700;padding-left:27px;line-height:30px">Project Timeline - 2024</div>
  <svg style="left:55px;top:125px" width="430" height="70" font-family="Poppins, sans-serif" font-size="6.5" font-weight="600">
    <line x1="45" y1="0" x2="45" y2="30" stroke="#2a7f7a" stroke-width="1.5"/><circle cx="45" cy="8" r="3" fill="#2a7f7a"/>
    <line x1="203" y1="0" x2="203" y2="30" stroke="#2a7f7a" stroke-width="1.5"/><circle cx="203" cy="8" r="3" fill="#2a7f7a"/>
    <line x1="361" y1="0" x2="361" y2="30" stroke="#2a7f7a" stroke-width="1.5"/><circle cx="361" cy="8" r="3" fill="#2a7f7a"/>
    <line x1="124" y1="40" x2="124" y2="65" stroke="#111" stroke-width="1.5"/><circle cx="124" cy="60" r="3" fill="#111"/>
    <line x1="282" y1="40" x2="282" y2="65" stroke="#111" stroke-width="1.5"/><circle cx="282" cy="60" r="3" fill="#111"/>
    <polygon points="10,40 0,30 78,30 88,40" fill="#2a7f7a"/><text x="45" y="38" text-anchor="middle" fill="#fff">1990</text>
    <polygon points="80,30 158,30 168,40 90,40" fill="#111" transform="translate(0,0)"/><text x="124" y="38" text-anchor="middle" fill="#fff">2001</text>
    <polygon points="168,40 158,30 238,30 248,40" fill="#2a7f7a"/><text x="203" y="38" text-anchor="middle" fill="#fff">2007</text>
    <polygon points="238,30 316,30 326,40 248,40" fill="#111"/><text x="282" y="38" text-anchor="middle" fill="#fff">2012</text>
    <polygon points="326,40 316,30 394,30 404,40" fill="#2a7f7a"/><text x="361" y="38" text-anchor="middle" fill="#fff">2020</text>
  </svg>
  <div style="left:60px;top:97px;width:80px;text-align:center"><div style="font-size:8px;font-weight:500">Your Title</div><div class="fine" style="font-size:6px">Refers to a good or service being offered</div></div>
  <div style="left:218px;top:97px;width:80px;text-align:center"><div style="font-size:8px;font-weight:500">Your Title</div><div class="fine" style="font-size:6px">Refers to a good or service being offered</div></div>
  <div style="left:376px;top:97px;width:80px;text-align:center"><div style="font-size:8px;font-weight:500">Your Title</div><div class="fine" style="font-size:6px">Refers to a good or service being offered</div></div>
  <div style="left:139px;top:212px;width:80px;text-align:center"><div style="font-size:8px;font-weight:500">Your Title</div><div class="fine" style="font-size:6px">Refers to a good or service being offered</div></div>
  <div style="left:297px;top:212px;width:80px;text-align:center"><div style="font-size:8px;font-weight:500">Your Title</div><div class="fine" style="font-size:6px">Refers to a good or service being offered</div></div>
  <div class="page-no">13</div>
</section>

<!-- 14 -->
<section class="slide" style="left:630px;top:1375px">
  <div role="img" aria-label="Teal-tinted photo of a modern office interior" style="left:0;top:0;width:187px;height:300px;background:linear-gradient(160deg,#3a8d88,#2a7f7a 60%,#24706c)"></div>
  <div style="left:30px;top:0;width:52px;height:300px;display:flex;align-items:center;justify-content:center"><span style="transform:rotate(90deg);color:#fff;font-weight:700;font-size:19px;letter-spacing:4px;white-space:nowrap">TEXT ADDED</span></div>
  <div class="bar-ink" style="left:103px;top:48px;width:189px;height:54px;color:#fff;font-size:15px;font-weight:600;padding-left:14px;line-height:54px;box-shadow:0 2px 4px rgba(0,0,0,.3)">1. Lorem Ipsum</div>
  <div class="bar-ink" style="left:103px;top:125px;width:189px;height:54px;color:#fff;font-size:15px;font-weight:600;padding-left:14px;line-height:54px;box-shadow:0 2px 4px rgba(0,0,0,.3)">2. Lorem Ipsum</div>
  <div class="bar-ink" style="left:103px;top:213px;width:189px;height:54px;color:#fff;font-size:15px;font-weight:600;padding-left:14px;line-height:54px;box-shadow:0 2px 4px rgba(0,0,0,.3)">3. Lorem Ipsum</div>
  <div class="h-bold" style="left:327px;top:85px;font-size:17px;line-height:1.25">Text<br>Added Hare</div>
  <div class="dash" style="left:327px;top:136px"></div>
  <div class="fine" style="left:327px;top:151px;width:180px">Lorem ipsum dolor sit amet, consectetuer adipiscing elit, sed diam nonummy nibh .<br><br>Ut wisi enim ad minim veniam, quis nostrud exerci tation ullamcorper suscipit lobortis. Ut wisi enim ad minim veniam, quis nostrud exerci tation ullamcorper suscipit</div>
  <div class="page-no">14</div>
</section>

<!-- 15 Steps -->
<section class="slide" style="left:1192px;top:1375px">
  <div class="bar-teal" style="left:0;top:0;width:534px;height:65px"></div>
  <div style="left:163px;top:42px;width:207px;height:46px;background:#2b2b2b;color:#fff;font-size:16px;font-weight:600;text-align:center;line-height:46px">Text Added Hare</div>
  <svg style="left:20px;top:105px" width="500" height="110" font-family="Poppins, sans-serif" font-size="5.5" font-weight="600" fill="#fff">
    <line x1="15" y1="65" x2="465" y2="65" stroke="#2a7f7a" stroke-width="5"/>
    <polygon points="462,58 475,65 462,72" fill="#2a7f7a"/>
    <g>
      <circle cx="102" cy="37" r="30" fill="#2a7f7a"/><circle cx="102" cy="37" r="21" fill="#fff"/><circle cx="102" cy="37" r="10" fill="none" stroke="#111" stroke-width="1.5"/><path d="M102 31 V37 H107" stroke="#111" stroke-width="1.5" fill="none"/>
      <circle cx="196" cy="37" r="30" fill="#2a7f7a"/><circle cx="196" cy="37" r="21" fill="#fff"/><circle cx="196" cy="40" r="8" fill="#111"/><rect x="193" y="28" width="6" height="4" fill="#111"/>
      <circle cx="290" cy="37" r="30" fill="#2a7f7a"/><circle cx="290" cy="37" r="21" fill="#fff"/><ellipse cx="290" cy="31" rx="9" ry="3" fill="none" stroke="#111" stroke-width="1.5"/><path d="M281 31 V43 A9 3 0 0 0 299 43 V31 M281 37 A9 3 0 0 0 299 37" fill="none" stroke="#111" stroke-width="1.5"/>
      <circle cx="383" cy="37" r="30" fill="#2a7f7a"/><circle cx="383" cy="37" r="21" fill="#fff"/><circle cx="386" cy="34" r="6" fill="none" stroke="#111" stroke-width="1.8"/><line x1="382" y1="38" x2="376" y2="44" stroke="#111" stroke-width="2"/>
      <text x="110" y="67" fill="#fff">Step 01</text><text x="204" y="67">Step 02</text><text x="298" y="67">Step 03</text><text x="391" y="67">Step 04</text>
      <g stroke="#888"><line x1="102" y1="72" x2="102" y2="88"/><line x1="196" y1="72" x2="196" y2="88"/><line x1="290" y1="72" x2="290" y2="88"/><line x1="383" y1="72" x2="383" y2="88"/></g>
    </g>
  </svg>
  <div style="left:72px;top:206px;width:100px;text-align:center"><div style="font-size:9px;font-weight:500">Lorem Ipsum</div><div class="fine" style="font-size:4.8px">Lorem ipsum dolor sit amet, consectetuer adipiscing elit, sed diam nonummy nibh euismod tincidunt ut laoreet dolore magna aliquam erat</div></div>
  <div style="left:166px;top:206px;width:100px;text-align:center"><div style="font-size:9px;font-weight:500">Lorem Ipsum</div><div class="fine" style="font-size:4.8px">Lorem ipsum dolor sit amet, consectetuer adipiscing elit, sed diam nonummy nibh euismod tincidunt ut laoreet dolore magna aliquam erat</div></div>
  <div style="left:260px;top:206px;width:100px;text-align:center"><div style="font-size:9px;font-weight:500">Lorem Ipsum</div><div class="fine" style="font-size:4.8px">Lorem ipsum dolor sit amet, consectetuer adipiscing elit, sed diam nonummy nibh euismod tincidunt ut laoreet dolore magna aliquam erat</div></div>
  <div style="left:353px;top:206px;width:100px;text-align:center"><div style="font-size:9px;font-weight:500">Lorem Ipsum</div><div class="fine" style="font-size:4.8px">Lorem ipsum dolor sit amet, consectetuer adipiscing elit, sed diam nonummy nibh euismod tincidunt ut laoreet dolore magna aliquam erat</div></div>
  <div class="page-no">15</div>
</section>

<!-- 22 Mobile -->
<section class="slide" style="left:67px;top:1701px">
  <div class="h-bold" style="left:35px;top:28px;font-size:26px;font-weight:800;line-height:1.2">Text<br><span class="teal">Added</span><br>Here</div>
  <div class="bar-teal" style="left:0;top:153px;width:200px;height:115px"></div>
  <div style="left:30px;top:162px;width:160px;display:flex;flex-direction:column;gap:9px">
    <div class="num-item"><b class="n">1.</b><div><div class="t" style="font-size:8.5px">Lorem Ipsum</div><div class="fine white" style="font-size:5.3px">Lorem ipsum dolor sit amet, consectetuer adipiscing elit, sed diam nonummy nibh euismod</div></div></div>
    <div class="num-item"><b class="n">2.</b><div><div class="t" style="font-size:8.5px">Lorem Ipsum</div><div class="fine white" style="font-size:5.3px">Lorem ipsum dolor sit amet, consectetuer adipiscing elit, sed diam nonummy nibh euismod</div></div></div>
    <div class="num-item"><b class="n">3.</b><div><div class="t" style="font-size:8.5px">Lorem Ipsum</div><div class="fine white" style="font-size:5.3px">Lorem ipsum dolor sit amet, consectetuer adipiscing elit, sed diam nonummy nibh euismod</div></div></div>
  </div>
  <div role="img" aria-label="Faint world map in the background" style="left:210px;top:60px;width:300px;height:170px;background:radial-gradient(ellipse at center,#ececec,#fff 70%)"></div>
  <div style="left:240px;top:45px;width:62px;height:135px;border:3px solid #222;border-radius:8px;background:#fff;padding:12px 5px"><div style="font-size:6px;font-weight:600;line-height:1.2">Lorem ipsum dolor</div><div style="margin:14px auto 6px;width:16px;height:11px;border:1px solid var(--teal)"></div><div class="fine" style="font-size:3.6px">To introduce the students to the changing landscape of marketing and equip them with knowledge and tools.</div></div>
  <div style="left:323px;top:85px;width:63px;height:135px;border:3px solid #222;border-radius:8px;background:#fff;padding:12px 5px"><div style="font-size:6px;font-weight:600;line-height:1.2">Dolor sit amet, conse</div><div style="margin:12px auto 6px;width:14px;height:14px;border:1px solid var(--teal);border-radius:3px"></div><div class="fine" style="font-size:3.6px">You will learn concepts and ideas in digital marketing as well as how to use tools.</div></div>
  <div style="left:404px;top:130px;width:64px;height:135px;border:3px solid #222;border-radius:8px;background:#fff;padding:12px 5px"><div style="font-size:6px;font-weight:600">Consec</div><div style="margin:22px auto 6px;width:14px;height:14px;border:1px solid var(--teal);border-radius:50%"></div><div class="fine" style="font-size:3.6px">You are required to pass 80% of the evaluation test to obtain the certificate.</div></div>
  <div class="page-no">22</div>
</section>

<!-- 23 Team -->
<section class="slide" style="left:630px;top:1701px">
  <div class="bar-teal" style="left:0;top:32px;width:534px;height:106px"></div>
  <div style="left:0;top:58px;width:534px;text-align:center;color:#fff;font-size:23px;font-weight:700">The Team Members</div>
  <div role="img" aria-label="Team member portrait" style="left:65px;top:116px;width:46px;height:46px;border-radius:50%;border:3px solid #fff;background:#cfd6d8"></div>
  <div role="img" aria-label="Team member portrait" style="left:182px;top:116px;width:46px;height:46px;border-radius:50%;border:3px solid #fff;background:#cfd6d8"></div>
  <div role="img" aria-label="Team member portrait" style="left:302px;top:116px;width:46px;height:46px;border-radius:50%;border:3px solid #fff;background:#cfd6d8"></div>
  <div role="img" aria-label="Team member portrait" style="left:422px;top:116px;width:46px;height:46px;border-radius:50%;border:3px solid #fff;background:#cfd6d8"></div>
  <div style="left:33px;top:168px;width:110px;text-align:center"><div style="font-size:8px;font-weight:600">ARLO BRENNAN</div><div class="fine" style="font-size:4.8px">Ipsum dolor sit amet, cons ectetuer adipiscing elit, sed diam nonummy nibh euismod tincidunt<br><br>ut laoreet dolore magna aliquam erat volutpat.</div></div>
  <div style="left:150px;top:168px;width:110px;text-align:center"><div style="font-size:8px;font-weight:600">NOLA KESTREL</div><div class="fine" style="font-size:4.8px">Ipsum dolor sit amet, cons ectetuer adipiscing elit, sed diam nonummy nibh euismod tincidunt<br><br>ut laoreet dolore magna aliquam erat volutpat.</div></div>
  <div style="left:270px;top:168px;width:110px;text-align:center"><div style="font-size:8px;font-weight:600">ARLO BRENNAN</div><div class="fine" style="font-size:4.8px">Ipsum dolor sit amet, cons ectetuer adipiscing elit, sed diam nonummy nibh euismod tincidunt<br><br>ut laoreet dolore magna aliquam erat volutpat.</div></div>
  <div style="left:390px;top:168px;width:110px;text-align:center"><div style="font-size:8px;font-weight:600">NOLA KESTREL</div><div class="fine" style="font-size:4.8px">Ipsum dolor sit amet, cons ectetuer adipiscing elit, sed diam nonummy nibh euismod tincidunt<br><br>ut laoreet dolore magna aliquam erat volutpat.</div></div>
  <div class="page-no">23</div>
</section>

<!-- Thank you -->
<section class="slide" style="left:1192px;top:1701px">
  <div role="img" aria-label="Teal-tinted photo of a data operations room" style="left:55px;top:0;width:430px;height:300px;background:linear-gradient(135deg,#3d8f8a,#2a7f7a 55%,#236d69)"></div>
  <div class="bar-ink" style="left:0;top:97px;width:230px;height:105px"></div>
  <div style="left:30px;top:108px;color:#fff;font-size:31px;font-weight:700">Thank You</div>
  <div class="fine white" style="left:32px;top:160px;width:150px;font-style:italic;color:#ddd">Lorem ipsum dolor sit amet, consectetuer adipiscing elit, sed diam nonum</div>
  <div class="bar-teal" style="left:214px;top:187px;width:12px;height:12px"></div>
  <svg style="left:258px;top:100px" width="30" height="100" fill="#fff">
    <path d="M6 4 L10 4 L12 9 L9 11 Q11 15 15 17 L17 14 L22 16 L22 20 Q14 21 8 14 Q3 8 6 4Z"/>
    <line x1="27" y1="2" x2="27" y2="22" stroke="#fff"/>
    <path d="M4 42 L22 36 L15 55 L12 46 Z"/>
    <line x1="27" y1="36" x2="27" y2="56" stroke="#fff"/>
    <path d="M3 80 L13 71 L23 80 H20 V90 H15 V84 H11 V90 H6 V80 Z"/>
    <line x1="27" y1="70" x2="27" y2="90" stroke="#fff"/>
  </svg>
  <div style="left:300px;top:101px;color:#fff;font-size:7px;line-height:1.3">+18 2555 0142 1808<br>+18 2555 0142 1808</div>
  <div style="left:300px;top:135px;color:#fff;font-size:7px;line-height:1.3">www.websitename.com<br>hello@lumeramail.com</div>
  <div style="left:300px;top:168px;color:#fff;font-size:7px;line-height:1.3">1234 Street name, town/city,<br>state/country, post/zip 012345.</div>
  <div class="bar-ink" style="left:485px;top:0;width:49px;height:38px"></div>
  <div style="left:509px;top:38px;width:1px;height:262px;background:var(--teal)"></div>
  <div style="left:485px;top:70px;width:49px;height:150px;display:flex;align-items:center;justify-content:center"><span style="transform:rotate(90deg);font-size:7px;letter-spacing:3px;white-space:nowrap;background:#fff;padding:0 4px;color:var(--teal-deep)">WWW.WEBSITE.COM</span></div>
</section>

</div>
</body>
</html>
```